House-share and Room Rental Website (With Focus on the Bedroom Landing Page)

Looking for website design for our House-share (executive accommodation) and room rental business.

Our company name is: Quellnest could also be written as QuellNest or quellnest. Either is fine .. just looking for a nice clean catchy logo to go with the design.

EXAMPLES
These are examples of other websites in this field that are doing well. this is a kind of baseline.
https://dovelinter.example.au/
https://www.kestrib.example/
https://www.velunor.example/
https://www.trisbel.example/
https://www.pondmarrowseek.example.au/

Our business model is to rent rooms to people looking for high-quality accommodation. We fill the gap between those looking to rent rooms and those with rooms to rent. However, our model is slightly different from those already on the market as we looking to fill a massive gap in the market delivering upmarket rooms for rent.(Executive Accommodation) also in the back end will be coupled with a self management process in the back end.

We offer executive style accommodation that stands out above the rest. With special extras like fire safety.. and management processes that create happier homes. We are looking for a web design package that can help us grow and scale our business. We need a design that is captivating

Our MAIN focus is having a room landing page that stands out from the rest... The core of our business will rely on the promotion of the rooms in a share house... so the whole design relies on the BEDROOM landing page to drive results.

Target Market(s)

We have 2 markets we are aiming at ... the first market is people offering rooms to rent who want the highest rental return. The second market is people looking to rent safe, high-quality rooms, in houses that are well managed and looked after.

Industry/Entity Type

Share Economy

Logo Text

QuellNest

Number of Pages Required

5+ page

Font styles to use
Sans Serif

Colors
3276b5

Requirements
Must have
• A messaging system whereby we can create direct communication between those offering rooms and those looking for rooms.
• A call to action that says " Schedule an Inspection"
• Landing page for promoting rooms
• A home page for showing stock.
• Profile page for those selling rooms
• Profile page for those looking for rooms.
• A scheduling calendar for booking inspections
Nice to have
• Pages where new residents can lock in a room.. pay bond and rents.. and sign contracts
• Notifications
• SMS capabilities in the backend.
Should not have
• No script or handwriting fonts.

```html
<!DOCTYPE html>
<html lang="en">
<head>
<meta charset="utf-8">
<title>QuellNest – Executive Room</title>
<link href="https://fonts.googleapis.com/css2?family=Jost:wght@300;400;500;600&display=swap" rel="stylesheet">
<style>
:root{
  --brand:#3276b5;
  --brand-dark:#25609a;
  --brand-panel:#5388c4;
  --ink:#1f2a36;
  --text:#4a4f55;
  --muted:#8a8f95;
  --line:#e3e5e8;
  --frame:#e9eaec;
  --white:#ffffff;
}
*{box-sizing:border-box;margin:0;padding:0}
html,body{width:1200px;height:3403px;overflow:hidden;background:var(--white)}
body{position:relative;font-family:"Jost",sans-serif;color:var(--text)}
.abs{position:absolute}

/* header */
.site-header{left:0;top:0;width:1200px;height:70px;background:linear-gradient(90deg,#2f6fae,var(--brand) 60%,#3a80c0)}
.brand{left:148px;top:12px;display:flex;align-items:center;gap:12px;color:var(--white)}
.brand-mark{width:40px;height:40px;border:2px solid var(--white);border-radius:4px}
.brand-name{font-size:30px;font-weight:400;line-height:1}
.brand-sub{font-size:13px;font-weight:300;margin-top:2px}
.search{left:454px;top:18px;width:317px;height:34px;background:var(--white);border-radius:17px;display:flex;align-items:center;padding-left:14px;gap:8px;font-size:13px;color:var(--muted)}
.nav{left:808px;top:26px;display:flex;gap:22px;font-size:13px;color:var(--white)}

/* hero */
.hero{left:0;top:70px;width:1200px;height:531px;
  background:
    radial-gradient(ellipse 420px 220px at 300px 330px,rgba(214,200,180,.55),rgba(214,200,180,0) 70%),
    radial-gradient(ellipse 380px 260px at 1010px 200px,rgba(210,220,200,.85),rgba(210,220,200,0) 75%),
    radial-gradient(ellipse 300px 160px at 1040px 420px,rgba(130,150,110,.7),rgba(130,150,110,0) 75%),
    linear-gradient(100deg,#1e1814 0%,#3a2e26 22%,#5c4b3d 42%,#7a6a58 58%,#8c9484 76%,#b9c0b2 100%)}
.hero-title{left:370px;top:234px;width:487px;height:47px;background:rgba(20,20,20,.78);color:var(--white);font-size:33px;font-weight:500;text-align:center;line-height:47px;letter-spacing:.5px}
.hero-copy{left:370px;top:286px;width:487px;text-align:center;color:var(--white);font-size:14px;line-height:19px}
.hero-btn{left:530px;top:347px;width:141px;height:28px;background:rgba(255,255,255,.2);border:1px solid rgba(255,255,255,.5);color:var(--white);font-size:14px;text-align:center;line-height:26px}
.thumb{top:488px;width:164px;height:93px;border:4px solid #5b5148}
.thumb.active{border-color:var(--brand)}
.arrow{top:516px;width:20px;height:36px}
.dot{left:597px;top:582px;width:7px;height:7px;border-radius:50%;background:var(--white)}

/* section titles */
.section-title{left:0;width:1200px;text-align:center;font-size:31px;font-weight:500;color:var(--ink);letter-spacing:.5px}
.section-title em{font-style:normal;color:var(--brand)}
.address{left:0;top:734px;width:1200px;display:flex;justify-content:center;align-items:center;gap:8px;font-size:14px}

/* details */
.details-card{left:141px;top:798px;width:512px;height:513px;background:var(--white);border:1px solid var(--line)}
.detail-row{left:168px;width:322px;height:30px;display:flex;align-items:center;font-size:13px}
.detail-label{width:179px;line-height:14px}
.detail-label small{display:block;font-size:10px;color:var(--muted)}
.detail-colon{width:36px}
.detail-value{width:107px;height:28px;border:1px solid var(--line);text-align:center;line-height:26px;font-size:12px;color:var(--muted)}
.btn{background:var(--brand);color:var(--white);text-align:center;font-size:16px}
.photo-frame{background:var(--frame);padding:18px}
.photo{width:100%;height:100%}

/* amenities */
.amen-card{left:547px;top:1973px;width:510px;height:529px;background:var(--white);border:1px solid var(--line)}
.amen-item{left:712px;display:flex;align-items:center;gap:22px;font-size:14px;color:var(--text)}
.amen-item svg{width:26px;height:26px}

.tagline{left:0;top:2586px;width:1200px;text-align:center;color:var(--brand);font-size:27px}
.tagline-sub{left:0;top:2628px;width:1200px;text-align:center;font-size:18px;line-height:28px;color:var(--ink);font-weight:400}

/* location */
.map{left:0;top:2824px;width:653px;height:465px;
  background:
    radial-gradient(ellipse 160px 260px at 500px 260px,rgba(170,200,225,.7),rgba(170,200,225,0) 75%),
    linear-gradient(135deg,#eceee7,#e4e8df 50%,#dde5e8)}
.map-card{left:213px;top:2980px;width:270px;height:154px;background:var(--brand);color:var(--white);font-size:11.5px;padding:14px 14px}
.map-card .row{display:flex;gap:10px;align-items:flex-start;margin-bottom:12px;line-height:15px;white-space:nowrap}
.map-card .ico{flex:none;width:22px;height:22px;border:1px solid var(--white);border-radius:50%}
.public{left:653px;top:2824px;width:547px;height:465px;background:var(--brand-panel);color:var(--white)}
.public h3{position:absolute;left:61px;top:140px;font-size:28px;font-weight:400}
.pub-item{left:714px;display:flex;align-items:center;gap:14px;font-size:13px;color:var(--white)}

/* footer */
.copyright{left:0;top:3320px;width:1200px;text-align:center;font-size:13px;color:var(--ink)}
.social{top:3353px;width:26px;height:26px;border-radius:50%;background:var(--brand)}
.footer-bar{left:0;top:3395px;width:1200px;height:8px;background:var(--brand)}
</style>
</head>
<body>

<header class="abs site-header">
  <div class="abs brand">
    <span class="brand-mark"></span>
    <div><div class="brand-name">quellnest</div><div class="brand-sub">Accomodation Rental</div></div>
  </div>
  <div class="abs search">
    <svg width="14" height="14" viewBox="0 0 14 14"><circle cx="6" cy="6" r="4.5" fill="none" stroke="#8a8f95" stroke-width="1.5"/><line x1="9.5" y1="9.5" x2="13" y2="13" stroke="#8a8f95" stroke-width="1.5"/></svg>
    Rooms for Rent
  </div>
  <nav class="abs nav"><span>Become a host</span><span>Help</span><span>Sign up</span><span>Log in</span></nav>
</header>

<section class="abs hero" role="img" aria-label="Photo of a luxury bedroom with a tufted bed and a window onto a lawn and trees"></section>
<h1 class="abs hero-title">DISCOVER YOUR BEST ROOM</h1>
<p class="abs hero-copy">Lorem ipsum dolor sit amet, consectetuer adipiscing elit, sed diam<br>nonummy nibh euismod tincidunt ut laoreet</p>
<div class="abs hero-btn">Discover Now</div>
<svg class="abs arrow" style="left:104px" viewBox="0 0 20 36"><polyline points="14,6 4,18 14,30" fill="none" stroke="#fff" stroke-width="3"/></svg>
<div class="abs thumb" style="left:143px;background:radial-gradient(circle at 60% 65%,#e8e0d2,rgba(232,224,210,0) 55%),linear-gradient(135deg,#3a2c22,#8a7560)" role="img" aria-label="Bedroom thumbnail"></div>
<div class="abs thumb" style="left:329px;background:radial-gradient(circle at 50% 40%,#d9a866,rgba(217,168,102,0) 60%),linear-gradient(135deg,#2e1a0e,#7a4e26)" role="img" aria-label="Bedroom thumbnail"></div>
<div class="abs thumb active" style="left:517px;background:radial-gradient(circle at 75% 35%,#d8dccb,rgba(216,220,203,0) 60%),linear-gradient(135deg,#3e362e,#a89d88)" role="img" aria-label="Bedroom thumbnail"></div>
<div class="abs thumb" style="left:705px;background:radial-gradient(circle at 45% 60%,#c0392b,rgba(192,57,43,0) 55%),linear-gradient(135deg,#e7d6c2,#b98f74)" role="img" aria-label="Bedroom thumbnail"></div>
<div class="abs thumb" style="left:891px;background:radial-gradient(circle at 50% 65%,#f2ece6,rgba(242,236,230,0) 55%),linear-gradient(135deg,#6b2f3a,#c9a99c)" role="img" aria-label="Bedroom thumbnail"></div>
<svg class="abs arrow" style="left:1074px" viewBox="0 0 20 36"><polyline points="6,6 16,18 6,30" fill="none" stroke="#fff" stroke-width="3"/></svg>
<span class="abs dot"></span>

<h2 class="abs section-title" style="top:683px"><em>EXECUTIVE</em> ROOM</h2>
<div class="abs address">
  <svg width="14" height="18" viewBox="0 0 14 18"><path d="M7 1a6 6 0 0 1 6 6c0 4-6 10-6 10S1 11 1 7a6 6 0 0 1 6-6z" fill="#3276b5"/><circle cx="7" cy="7" r="2.2" fill="#fff"/></svg>
  123, Lorem ipsum Ltd.., 21 Lorem &nbsp;Street, Lorem ipsum - 123 456
</div>

<div class="abs details-card"></div>
<div class="abs detail-row" style="top:839px"><span class="detail-label">Gender Preference</span><span class="detail-colon">:</span><span class="detail-value">Male</span></div>
<div class="abs detail-row" style="top:876px"><span class="detail-label">Room type</span><span class="detail-colon">:</span><span class="detail-value">Private</span></div>
<div class="abs detail-row" style="top:913px"><span class="detail-label">Size of Room</span><span class="detail-colon">:</span><span class="detail-value">10 Sqm</span></div>
<div class="abs detail-row" style="top:954px"><span class="detail-label">Minimum contract term<small>(usually 3 months)</small></span><span class="detail-colon">:</span><span class="detail-value">4 months</span></div>
<div class="abs detail-row" style="top:992px"><span class="detail-label">Type of housemates</span><span class="detail-colon">:</span><span class="detail-value">Professionals</span></div>
<div class="abs detail-row" style="top:1030px"><span class="detail-label">Bed Size (in)</span><span class="detail-colon">:</span><span class="detail-value">54" X 75"</span></div>
<div class="abs detail-row" style="top:1067px"><span class="detail-label">Bathroom</span><span class="detail-colon">:</span><span class="detail-value">Shared</span></div>
<div class="abs detail-row" style="top:1105px"><span class="detail-label">Preference</span><span class="detail-colon">:</span><span class="detail-value">Smoking</span></div>
<div class="abs detail-row" style="top:1143px"><span class="detail-label">Images of the room</span><span class="detail-colon">:</span><span class="detail-value">Available</span></div>
<div class="abs detail-row" style="top:1182px"><span class="detail-label">Images of the house<br>and amenities</span><span class="detail-colon">:</span><span class="detail-value">Yes</span></div>
<div class="abs btn" style="left:166px;top:1236px;width:324px;height:34px;line-height:34px">Rental Price - 150 $ &#8964;</div>

<div class="abs photo-frame" style="left:547px;top:839px;width:512px;height:431px">
  <div class="photo" style="background:
    radial-gradient(ellipse 120px 150px at 72% 62%,rgba(235,225,215,.85),rgba(235,225,215,0) 75%),
    radial-gradient(ellipse 160px 90px at 40% 25%,rgba(200,170,130,.7),rgba(200,170,130,0) 75%),
    linear-gradient(180deg,#4a3a2c 0%,#7a6048 35%,#5a4a3e 60%,#8a8078 100%)" role="img" aria-label="Photo of a hand holding a phone showing the booking app in front of a hotel-style bedroom"></div>
</div>

<p class="abs section-title" style="top:1355px;font-size:16px;font-weight:400;color:var(--muted)">about the quellnest</p>
<h2 class="abs section-title" style="top:1391px"><span style="font-weight:400">A</span> <em>BEST PLACE</em> TO ENJOY YOUR LIFE</h2>

<div class="abs" style="left:0;top:1460px;width:1200px;height:281px;background:
  radial-gradient(ellipse 300px 80px at 900px 60px,rgba(220,120,90,.7),rgba(220,120,90,0) 75%),
  linear-gradient(180deg,#2b2a5a 0%,#6a4a70 30%,#b46a5e 52%,#2a3a6a 72%,#16224a 100%)" role="img" aria-label="City skyline at dusk"></div>
<div class="abs photo-frame" style="left:141px;top:1578px;width:918px;height:309px;padding:12px">
  <div class="photo" style="background:
    radial-gradient(ellipse 240px 70px at 50% 48%,rgba(245,243,240,.95),rgba(245,243,240,0) 75%),
    linear-gradient(180deg,#2e2c2b 0%,#4a4644 40%,#6a625c 58%,#7a5a40 78%,#9a7452 100%)" role="img" aria-label="Photo of a modern bedroom with a grey bed, pendant lamps and wooden floor"></div>
</div>

<div class="abs amen-card"></div>
<div class="abs photo-frame" style="left:141px;top:2021px;width:512px;height:433px">
  <div class="photo" style="background:
    radial-gradient(ellipse 60px 110px at 45% 48%,rgba(70,130,200,.8),rgba(70,130,200,0) 80%),
    radial-gradient(ellipse 60px 60px at 75% 62%,rgba(190,160,120,.8),rgba(190,160,120,0) 80%),
    linear-gradient(180deg,#8d8f93 0%,#b8babd 30%,#eeeeef 55%,#f4f4f4 80%,#d8d6d2 100%)" role="img" aria-label="Photo of a guest seated on a white bed beside a suitcase"></div>
</div>
<h2 class="abs" style="left:712px;top:2037px;font-size:30px;font-weight:500;color:var(--ink)"><span style="color:var(--brand)">ROOM</span> AMENITIES</h2>
<div class="abs amen-item" style="top:2100px"><svg viewBox="0 0 26 26" fill="none" stroke="#555" stroke-width="1.3"><rect x="3" y="4" width="14" height="18"/><line x1="3" y1="13" x2="17" y2="13"/><rect x="17" y="10" width="6" height="12"/></svg>Furnished</div>
<div class="abs amen-item" style="top:2144px"><svg viewBox="0 0 26 26" fill="none" stroke="#555" stroke-width="1.3"><rect x="2" y="5" width="22" height="14"/><line x1="9" y1="22" x2="17" y2="22"/></svg>TV</div>
<div class="abs amen-item" style="top:2189px"><svg viewBox="0 0 26 26" fill="none" stroke="#555" stroke-width="1.3"><rect x="4" y="3" width="18" height="20"/><line x1="4" y1="10" x2="22" y2="10"/><line x1="4" y1="16" x2="22" y2="16"/></svg>Storage Space</div>
<div class="abs amen-item" style="top:2233px"><svg viewBox="0 0 26 26" fill="none" stroke="#555" stroke-width="1.3"><line x1="2" y1="13" x2="24" y2="13"/><line x1="5" y1="13" x2="5" y2="23"/><line x1="21" y1="13" x2="21" y2="23"/><rect x="8" y="4" width="10" height="7"/></svg>Study Desk / Workstation</div>
<div class="abs amen-item" style="top:2278px"><svg viewBox="0 0 26 26" fill="none" stroke="#555" stroke-width="1.3"><rect x="3" y="3" width="20" height="20"/><line x1="13" y1="3" x2="13" y2="23"/><rect x="5" y="6" width="6" height="6"/></svg>Wardrobe</div>
<div class="abs amen-item" style="top:2323px"><svg viewBox="0 0 26 26" fill="none" stroke="#555" stroke-width="1.3"><path d="M4 14h18v4a4 4 0 0 1-4 4H8a4 4 0 0 1-4-4z"/><path d="M8 14V6a3 3 0 0 1 6 0"/></svg>Ensuite Shower</div>
<div class="abs amen-item" style="top:2367px"><svg viewBox="0 0 26 26" fill="none" stroke="#555" stroke-width="1.3"><rect x="3" y="4" width="20" height="18"/><line x1="3" y1="11" x2="23" y2="11"/><circle cx="9" cy="16" r="2.5"/><circle cx="17" cy="16" r="2.5"/></svg>Kitchenette</div>
<div class="abs btn" style="left:710px;top:2420px;width:197px;height:32px;line-height:32px">Show All Amenities</div>

<p class="abs tagline">We offer executive style accommodation that stands out above the rest.</p>
<p class="abs tagline-sub">With special extras like fire safety and management processes that<br>create happier homes.</p>
<div class="abs btn" style="left:492px;top:2694px;width:220px;height:35px;line-height:35px">Schedule An Inspection</div>

<div class="abs map" role="img" aria-label="Street map of the area around the property"></div>
<div class="abs map-card">
  <div class="row"><span class="ico"></span><span>QUELLNEST<br>123, Lorem ipsum Ltd.., 21 Lorem &nbsp;Street,<br>Lorem ipsum sed ipsum - 123 456</span></div>
  <div class="row" style="align-items:center"><span class="ico"></span><span>123-456-7890</span></div>
  <div class="row" style="align-items:center;margin:0"><span class="ico"></span><span>info@quellnest.com</span></div>
</div>
<svg class="abs" style="left:505px;top:3020px" width="30" height="40" viewBox="0 0 30 40"><path d="M15 1a13 13 0 0 1 13 13c0 10-13 25-13 25S2 24 2 14A13 13 0 0 1 15 1z" fill="#3276b5"/><circle cx="15" cy="14" r="5" fill="#fff"/></svg>

<section class="abs public"><h3>PUBLIC AMENITIES</h3></section>
<div class="abs pub-item" style="top:3024px"><svg width="16" height="16" viewBox="0 0 16 16"><rect x="3" y="1" width="10" height="11" rx="2" fill="#fff"/><line x1="4" y1="15" x2="6" y2="12" stroke="#fff" stroke-width="1.5"/><line x1="12" y1="15" x2="10" y2="12" stroke="#fff" stroke-width="1.5"/></svg>0.5 km from railway station</div>
<div class="abs pub-item" style="top:3057px"><svg width="16" height="16" viewBox="0 0 16 16"><rect x="2" y="1" width="12" height="12" rx="2" fill="#fff"/><rect x="3" y="13" width="3" height="2" fill="#fff"/><rect x="10" y="13" width="3" height="2" fill="#fff"/></svg>1 km from bus stop</div>
<div class="abs pub-item" style="top:3090px"><svg width="16" height="16" viewBox="0 0 16 16"><path d="M2 9l5-1 4-6h2l-2 6 4 1v2l-4-1-2 5H7l1-5-6 1z" fill="#fff"/></svg>5 km's from airport</div>
<div class="abs pub-item" style="top:3123px"><svg width="16" height="16" viewBox="0 0 16 16"><path d="M8 1a5 5 0 0 1 5 5c0 4-5 9-5 9S3 10 3 6a5 5 0 0 1 5-5z" fill="#fff"/><circle cx="8" cy="6" r="1.8" fill="#5388c4"/></svg>Map of the area and shortest route the city</div>

<footer>
  <p class="abs copyright">Copyright © 2019 quellnest. All Rights Reserved.</p>
  <span class="abs social" style="left:534px"></span>
  <span class="abs social" style="left:569px;background:#3aa3e0"></span>
  <span class="abs social" style="left:604px;background:#2a74b0"></span>
  <span class="abs social" style="left:639px;background:#d9473a"></span>
  <div class="abs footer-bar"></div>
</footer>

</body>
</html>
```